Rental Services: Chair Covers, Sashes, Napkins, Table Cloth, Overlays, Cutlery, Plates, Glasses. Event Services: Weddings, Birthdays, Anniversaries, any Special Occasion Parties, Wedding and Birthday Cakes, and Catering including Vegan/Vegetarian Cuisine.
Industry/Entity Type
Event
Contact Information for Business Card
The name of the business is Vellmont Grove.
I need something with a little more flair to it.
I would like the color of the card to be a faded green on the back , the business name, logo and motto, the services that are being provided in two column Rental Services on one side and Event Services on the other side , my name, ph.#, email address and web page, an image of 2 champagne glass, wedding bands and a graduation cap.
On the front of the card I would like a picture of a banquet set with a business name, logo, business motto, my name, email address, website and phone #.
The business motto is "Bringing a Touch of Grace to every Lasting Occasion."
For the Business Name
Vellmont in bold black font with a Eiffel tower over the letter "a" in Vellmont and a champagne glass for the letter "I" in Vellmont. The Flair in a green color and "AR DECODE" font. then put the business motto under the business name in "AR DECODE" font in black. I have uploaded to images as a guide.Thanks
Font styles to use
Look and feel
Each slider illustrates characteristics of the customer's brand and the style your logo design should communicate.

```html
<!DOCTYPE html>
<html lang="en">
<head>
<meta charset="utf-8">
<title>Vellmont Grove – Business Card</title>
<link rel="stylesheet" href="https://fonts.googleapis.com/css2?family=Open+Sans:wght@400;600&family=Pinyon+Script&display=swap">
<style>
  :root {
    --page: #2a2a2a;
    --green: #8c9a5c;
    --green-dark: #6f7d43;
    --green-light: #b9c48e;
    --sage: #c9cfb6;
    --band: rgba(240, 244, 226, 0.55);
    --ink: #1d1d1d;
    --white: #ffffff;
  }
  * { margin: 0; padding: 0; box-sizing: border-box; }
  html, body { width: 1200px; height: 1000px; overflow: hidden; }
  body {
    background: var(--page);
    font-family: "Open Sans", sans-serif;
    position: relative;
  }
  .card {
    position: absolute;
    left: 220px;
    width: 760px;
    height: 434px;
    border-radius: 14px;
    overflow: hidden;
  }
  .card-back { top: 50px; background: linear-gradient(160deg, var(--green-light) 0%, var(--green) 45%, var(--green-dark) 100%); }
  .card-front { top: 516px; }

  .art { position: absolute; }
  .art-cap { left: 440px; top: 0; width: 320px; height: 170px; background: linear-gradient(200deg, rgba(60,70,35,0.55), rgba(140,154,92,0)); }
  .art-rings { left: 560px; top: 210px; width: 180px; height: 140px; border-radius: 50%; background: radial-gradient(circle, rgba(230,236,210,0.45), rgba(140,154,92,0) 70%); }
  .art-glasses { left: 0; top: 250px; width: 140px; height: 184px; background: linear-gradient(90deg, rgba(225,232,200,0.45), rgba(140,154,92,0)); }
  .art-banquet { inset: 0; background: linear-gradient(180deg, #9ea386 0%, #b7bca2 35%, var(--sage) 60%, #d9dccb 100%); }

  .band { position: absolute; left: 0; right: 0; background: var(--band); }
  .card-back .band { top: 196px; height: 52px; }
  .card-front .band { top: 250px; height: 50px; }

  .brand {
    position: absolute;
    color: var(--ink);
    font-weight: 600;
    letter-spacing: 1px;
    text-transform: uppercase;
    display: flex;
    align-items: center;
    gap: 12px;
  }
  .brand-dot { width: 14px; height: 14px; border-radius: 50%; background: var(--ink); }
  .card-back .brand { left: 36px; top: 122px; font-size: 34px; }
  .card-front .brand { left: 100px; top: 160px; font-size: 46px; }

  .contact { position: absolute; color: var(--white); font-size: 15px; line-height: 24px; text-transform: uppercase; text-align: right; }
  .card-back .contact { right: 36px; top: 40px; }
  .card-front .contact { right: 36px; top: 330px; color: var(--ink); font-size: 17px; line-height: 26px; }

  .services { position: absolute; top: 206px; color: var(--white); text-transform: uppercase; }
  .services h2 { font-size: 17px; font-weight: 400; letter-spacing: 0.5px; color: var(--ink); margin-bottom: 18px; }
  .services ul { list-style: none; font-size: 15px; line-height: 20px; }
  .services-rental { left: 150px; }
  .services-event { left: 400px; }

  .motto {
    position: absolute;
    left: 0; right: 0; top: 254px;
    text-align: center;
    font-family: "Pinyon Script", cursive;
    font-size: 30px;
    color: var(--ink);
  }
  .owner { position: absolute; left: 70px; top: 366px; color: var(--ink); font-size: 17px; line-height: 26px; text-transform: uppercase; }
</style>
</head>
<body>

<section class="card card-back">
  <div class="art art-cap" role="img" aria-label="Graduation cap and rolled diploma photo"></div>
  <div class="art art-rings" role="img" aria-label="Pair of wedding bands photo"></div>
  <div class="art art-glasses" role="img" aria-label="Two champagne glasses toasting photo"></div>
  <div class="band"></div>

  <div class="brand"><span class="brand-dot"></span>Vellmont Grove</div>

  <div class="contact">
    404 555 0172<br>
    hello@vellmontgrove.com<br>
    www.vellmontgrove.com
  </div>

  <div class="services services-rental">
    <h2>Rental Services:</h2>
    <ul>
      <li>Chair Covers and Sashes</li>
      <li>Table Cloth</li>
      <li>Napkins</li>
      <li>Overlays</li>
      <li>Cutleries</li>
      <li>Plates</li>
      <li>Glasses</li>
    </ul>
  </div>

  <div class="services services-event">
    <h2>Event Services:</h2>
    <ul>
      <li>Weddings</li>
      <li>Birthdays</li>
      <li>Anniversary</li>
      <li>Special Occasion Parties</li>
      <li>Office Functions</li>
      <li>Wedding &amp; Birthday Cakes</li>
      <li>Catering Including</li>
      <li>Vegan / Vegetarian Food</li>
    </ul>
  </div>
</section>

<section class="card card-front">
  <div class="art art-banquet" role="img" aria-label="Banquet table set with napkins, glasses and cutlery photo"></div>
  <div class="band"></div>

  <div class="brand"><span class="brand-dot"></span>Vellmont Grove</div>

  <p class="motto">Bringing a Touch of Grace to every Lasting Occasion</p>

  <div class="contact">
    hello@vellmontgrove.com<br>
    www.vellmontgrove.com
  </div>

  <div class="owner">
    Delia Hart Ambrose<br>
    404 555 0172
  </div>
</section>

</body>
</html>
```